Recreate a label for a champagne bottle [See attached example]

I'm needing to recreate a label for a champagne bottle label to give as closing gifts to clients when they purchase a home. Please include the following text "Welcome Home", my initials "R.T", "Established Year", the hashtag #BubTORVA and my logo (attached). I prefer to have a black or white background with a crisp, easy to read cursive font similar to the Dunmore bourbon font. I want it to look as similar of a layout to the Valdorca label as possible

Target Market(s)

Luxury

Font styles to use
Decorative
Script

Colors

Designer to choose only greyscale colors for use in the design.

Requirements
Must have
• "Welcome Home", my initials "R.T", "Established Year", the hashtag #BubTORVA and my logo
Nice to have
• Clean cursive font, easy to read, luxury look.
Should not have
• Clutter, too much design.

```html
<!DOCTYPE html>
<html lang="en">
<head>
<meta charset="utf-8">
<title>Welcome Home – Bottle Label</title>
<link rel="stylesheet" href="https://fonts.googleapis.com/css2?family=Montserrat:wght@500;600;700&family=Pinyon+Script&display=swap">
<style>
  :root {
    --backdrop: #f0f0ef;
    --label-white: #ffffff;
    --gold-light: #f3e2a4;
    --gold-mid: #d8bd72;
    --gold-deep: #b8974f;
    --ink-script: #4a4a4a;
    --ink-soft: #9c9c9c;
    --ink-mark: #8a8a8a;
  }
  * { box-sizing: border-box; margin: 0; padding: 0; }
  html, body {
    width: 1200px;
    height: 900px;
    overflow: hidden;
    background: var(--backdrop);
  }
  .canvas {
    width: 1200px;
    height: 900px;
    display: flex;
    align-items: center;
    justify-content: center;
  }
  .label {
    position: relative;
    width: 640px;
    height: 565px;
    padding: 16px;
    background: linear-gradient(135deg, var(--gold-deep) 0%, var(--gold-light) 35%, var(--gold-mid) 60%, var(--gold-light) 80%, var(--gold-deep) 100%);
  }
  .label-face {
    position: relative;
    width: 100%;
    height: 100%;
    background: var(--label-white);
    display: flex;
    flex-direction: column;
    align-items: center;
    font-family: "Montserrat", sans-serif;
  }
  .established {
    margin-top: 78px;
    display: flex;
    align-items: center;
    gap: 22px;
    font-size: 16px;
    font-weight: 600;
    letter-spacing: 0.38em;
    color: var(--ink-soft);
  }
  .brand-name {
    display: flex;
    align-items: center;
    gap: 8px;
    font-size: 16px;
    font-weight: 600;
    letter-spacing: 0.2em;
    color: var(--ink-mark);
  }
  .brand-square {
    width: 14px;
    height: 14px;
    background: var(--ink-mark);
  }
  .title {
    margin-top: 20px;
    font-family: "Pinyon Script", cursive;
    font-weight: 400;
    color: var(--ink-script);
    line-height: 0.82;
    text-align: center;
  }
  .title-line { display: block; font-size: 128px; }
  .title-line--first { margin-left: -30px; }
  .title-line--second { margin-left: 20px; }
  .hashtag {
    margin-top: 46px;
    font-size: 24px;
    font-weight: 700;
    letter-spacing: 0.2em;
    color: var(--gold-mid);
  }
  .initials {
    margin-top: 22px;
    font-size: 30px;
    font-weight: 600;
    letter-spacing: 0.12em;
    color: var(--ink-soft);
  }
</style>
</head>
<body>
  <main class="canvas">
    <section class="label" aria-label="Champagne bottle label">
      <div class="label-face">
        <p class="established">
          <span>ESTD</span>
          <span class="brand-name"><span class="brand-square"></span>TORVA</span>
          <span>2023</span>
        </p>
        <h1 class="title">
          <span class="title-line title-line--first">Welcome</span>
          <span class="title-line title-line--second">Home</span>
        </h1>
        <p class="hashtag">#BubTORVA</p>
        <p class="initials">R.T</p>
      </div>
    </section>
  </main>
</body>
</html>
```